MIRVEL soap beauty bar

I need a box designed to put a 4oz bar of soap inside. All sides of the box need design. A refreshingly fragrant blend of citrus and spicy notes, it is made with a blend of essential oils including ginger, mandarin, lemon and orange flowers

Target Market(s)

Homeless people

Requirements
Must have
• My company logo as pictured with text and design like a standard bar of soap. Weight 4oz, ingredients:
Olive oil, Coconut oil,Organic sustainable palm oil,Water,Lye,Shea butter, orange, ginger, mandarin, lemon essential oil. uploading pics for inspiration.
Nice to have
• The soap box measurements are Dimensions (L x W x H). 5.75 x 3.80 x 5.60 Inches ...

```html
<!DOCTYPE html>
<html lang="en">
<head>
<meta charset="utf-8">
<title>MIRVEL Body Soap – Box Dieline</title>
<link rel="stylesheet" href="https://fonts.googleapis.com/css2?family=Montserrat:wght@400;500;700&display=swap">
<style>
  :root {
    --page: #ffffff;
    --cut-line: #111111;
    --gold: #f4b400;
    --gold-soft: #f9d77a;
    --gold-deep: #d9a21a;
    --cream: #fbf6ea;
    --leaf-tint: #f1e6cf;
    --brand-green: #1f8f3a;
    --brand-red: #d2222d;
    --ribbon: #f0c04a;
    --ribbon-text: #6e5a1e;
    --copy-pale: #fbe6a6;
    --ink: #1a1a1a;
  }
  html, body {
    margin: 0;
    padding: 0;
    width: 1200px;
    height: 2546px;
    overflow: hidden;
    background: var(--page);
  }
  .dieline {
    position: absolute;
    left: 20px;
    top: 509px;
    width: 1160px;
    height: 1528px;
  }
  .type { font-family: 'Montserrat', sans-serif; }
  .brand-name { font-family: 'Montserrat', sans-serif; font-weight: 700; fill: var(--brand-green); }
  .brand-dot { fill: var(--brand-red); }
  .title { font-family: 'Montserrat', sans-serif; font-weight: 700; fill: #ffffff; font-size: 11.5px; }
  .tagline { font-family: 'Montserrat', sans-serif; font-weight: 500; fill: var(--copy-pale); font-size: 7.5px; }
  .description { font-family: 'Montserrat', sans-serif; font-weight: 500; fill: var(--copy-pale); font-size: 6.3px; }
  .ingredients { font-family: 'Montserrat', sans-serif; font-weight: 500; fill: var(--ink); font-size: 6.2px; }
  .net-content { font-family: 'Montserrat', sans-serif; font-weight: 400; fill: var(--ink); font-size: 6.3px; }
  .new-badge { font-family: 'Montserrat', sans-serif; font-weight: 700; fill: var(--ribbon-text); font-size: 12px; }
  .cut { fill: none; stroke: var(--cut-line); stroke-width: 1.2; stroke-linejoin: round; }
  .plain-flap { fill: #ffffff; stroke: var(--cut-line); stroke-width: 1.2; stroke-linejoin: round; }
  .icon-stroke { fill: none; stroke: var(--brand-green); stroke-width: 1.4; stroke-linecap: round; }
</style>
</head>
<body>
<svg class="dieline" viewBox="18 478 574 756" xmlns="http://www.w3.org/2000/svg" role="group" aria-label="MIRVEL body soap box, flat dieline">
  <defs>
    <linearGradient id="gold-fade-down" x1="0" y1="0" x2="0" y2="1">
      <stop offset="0" stop-color="var(--gold)"/>
      <stop offset="0.6" stop-color="var(--gold-soft)"/>
      <stop offset="1" stop-color="#ffffff"/>
    </linearGradient>
    <linearGradient id="gold-fade-up" x1="0" y1="1" x2="0" y2="0">
      <stop offset="0" stop-color="var(--gold)"/>
      <stop offset="0.55" stop-color="var(--gold-soft)"/>
      <stop offset="1" stop-color="#ffffff"/>
    </linearGradient>
    <linearGradient id="label-band" x1="0" y1="0" x2="1" y2="0">
      <stop offset="0" stop-color="var(--gold)"/>
      <stop offset="0.55" stop-color="#f6c434"/>
      <stop offset="1" stop-color="var(--gold-soft)"/>
    </linearGradient>
    <linearGradient id="tagline-band" x1="0" y1="0" x2="1" y2="0">
      <stop offset="0" stop-color="var(--gold-deep)"/>
      <stop offset="1" stop-color="var(--gold-soft)" stop-opacity="0.4"/>
    </linearGradient>
    <linearGradient id="produce-photo" x1="0" y1="0" x2="1" y2="1">
      <stop offset="0" stop-color="#e8cfa6"/>
      <stop offset="0.5" stop-color="#f5cf2e"/>
      <stop offset="1" stop-color="#f2b81c"/>
    </linearGradient>
    <linearGradient id="leaf-pattern" x1="0" y1="0" x2="1" y2="1">
      <stop offset="0" stop-color="var(--cream)"/>
      <stop offset="1" stop-color="var(--leaf-tint)"/>
    </linearGradient>

    <g id="front-face">
      <rect x="143" y="885" width="319" height="115" fill="url(#leaf-pattern)" role="img" aria-label="Faint leaf and branch pattern"/>
      <circle class="brand-dot" cx="186" cy="960" r="8"/>
      <text class="brand-name" x="199" y="967" font-size="19">MIRVEL</text>
      <rect x="305" y="903" width="157" height="97" rx="6" fill="url(#produce-photo)" role="img" aria-label="Photo of whole lemons, a lemon slice, mint leaves and ginger root"/>
      <rect x="143" y="1000" width="319" height="15" fill="url(#tagline-band)"/>
      <text class="tagline" x="155" y="1010.5">Made with natural Oils</text>
      <rect x="143" y="1015" width="319" height="70" fill="url(#label-band)"/>
      <text class="title" x="155" y="1033">BODY SOAP WITH</text>
      <text class="title" x="155" y="1047">CITRUS AND SPICE BLEND</text>
      <text class="description" x="155" y="1062">Soap made with a blend of essential oils including</text>
      <text class="description" x="155" y="1071">ginger, mandarin, lemon and orange flowers.</text>
    </g>
  </defs>

  <!-- Top tuck flap -->
  <path d="M143 527 L143 505 L155 484 L450 484 L462 505 L462 527 Z" fill="url(#gold-fade-down)"/>
  <path class="cut" d="M143 527 L143 505 L155 484 L450 484 L462 505 L462 527"/>

  <!-- Back panel (upside down) -->
  <rect x="143" y="527" width="319" height="223" fill="url(#leaf-pattern)"/>
  <use href="#front-face" transform="rotate(180 302.5 811.5)"/>
  <text class="net-content" x="302.5" y="540" transform="rotate(180 302.5 538)" text-anchor="end" dx="-140">Net content: 4oz</text>

  <!-- Back side flaps -->
  <path d="M143 537 L60 537 L55 545 L40 548 L25 560 L25 690 L35 700 L50 700 L50 725 L60 740 L143 740 Z" fill="url(#leaf-pattern)" role="img" aria-label="Faint leaf pattern"/>
  <path class="cut" d="M143 537 L60 537 L55 545 L40 548 L25 560 L25 690 L35 700 L50 700 L50 725 L60 740 L143 740"/>
  <path d="M462 537 L545 537 L550 545 L565 548 L580 560 L580 690 L570 700 L555 700 L555 725 L545 740 L462 740 Z" fill="url(#leaf-pattern)" role="img" aria-label="Faint leaf pattern"/>
  <path class="cut" d="M462 537 L545 537 L550 545 L565 548 L580 560 L580 690 L570 700 L555 700 L555 725 L545 740 L462 740"/>

  <!-- Top end panel (upside down) -->
  <rect x="143" y="750" width="215" height="130" fill="url(#gold-fade-up)"/>
  <g transform="rotate(180 250 800)">
    <text class="ingredients" x="188" y="782">Ingredients:</text>
    <text class="ingredients" x="188" y="791">Olive oil, Coconut oil,Organic sustainable palm</text>
    <text class="ingredients" x="188" y="800">oil,Water,Lye,Shea butter, orange, ginger,</text>
    <text class="ingredients" x="188" y="809">mandarin, lemon essential oil.</text>
    <circle class="brand-dot" cx="297" cy="839" r="6"/>
    <text class="brand-name" x="306" y="843" font-size="11">MIRVEL</text>
  </g>
  <rect x="358" y="750" width="104" height="130" fill="var(--gold)"/>
  <g transform="rotate(180 410 808)">
    <circle class="brand-dot" cx="410" cy="822" r="20"/>
    <text class="brand-name" x="410" y="790" font-size="14" text-anchor="middle">MIRVEL</text>
  </g>
  <path d="M358 865 L462 865 L462 905 L410 913 L358 905 Z" fill="var(--ribbon)"/>

  <!-- Top end side flaps -->
  <path class="plain-flap" d="M143 752 L75 752 L45 790 L45 868 L143 878"/>
  <path class="plain-flap" d="M462 752 L530 752 L560 790 L560 868 L462 878"/>

  <!-- Front panel -->
  <rect x="143" y="885" width="319" height="200" fill="url(#leaf-pattern)"/>
  <use href="#front-face"/>
  <path d="M358 880 L462 880 L462 905 L410 913 L358 905 Z" fill="var(--ribbon)"/>
  <text class="new-badge" x="410" y="899" text-anchor="middle">NEW!</text>

  <!-- Front side flaps -->
  <path d="M143 888 L60 888 L50 900 L30 905 L25 915 L25 1050 L40 1060 L55 1062 L58 1085 L143 1085 Z" fill="url(#leaf-pattern)" role="img" aria-label="Faint leaf pattern"/>
  <path class="cut" d="M143 888 L60 888 L50 900 L30 905 L25 915 L25 1050 L40 1060 L55 1062 L58 1085 L143 1085"/>
  <g transform="rotate(90 66 985)">
    <circle class="brand-dot" cx="28" cy="985" r="7"/>
    <text class="brand-name" x="40" y="991" font-size="16">MIRVEL</text>
  </g>
  <path d="M462 888 L545 888 L555 900 L575 905 L580 915 L580 1050 L565 1060 L550 1062 L547 1085 L462 1085 Z" fill="url(#leaf-pattern)" role="img" aria-label="Faint leaf pattern"/>
  <path class="cut" d="M462 888 L545 888 L555 900 L575 905 L580 915 L580 1050 L565 1060 L550 1062 L547 1085 L462 1085"/>
  <g transform="rotate(90 525 985)">
    <circle class="brand-dot" cx="487" cy="985" r="7"/>
    <text class="brand-name" x="499" y="991" font-size="16">MIRVEL</text>
  </g>

  <text class="net-content" x="458" y="1097" text-anchor="end">Net content: 4oz</text>

  <!-- Bottom end panel -->
  <rect x="143" y="1100" width="319" height="128" fill="url(#gold-fade-up)"/>
  <circle class="brand-dot" cx="272" cy="1158" r="7"/>
  <text class="brand-name" x="284" y="1164" font-size="15">MIRVEL</text>
  <g aria-label="Recyclable" role="img">
    <path class="icon-stroke" d="M152 1114 A7 7 0 1 1 158 1125"/>
    <path class="icon-stroke" d="M155 1121 L158 1125 L154 1128"/>
  </g>

  <!-- Bottom end flaps and glue strip -->
  <path class="plain-flap" d="M143 1092 L62 1092 L45 1110 L45 1228 L143 1228"/>
  <path class="plain-flap" d="M462 1092 L545 1092 L558 1110 L558 1228 L462 1228"/>

  <!-- Main cut lines -->
  <path class="cut" d="M143 527 L143 1228 L462 1228 L462 527"/>
</svg>
</body>
</html>
```